Website for The Tavery Parlour

I require a website for "The Tavery Parlour" which is a blog type business for 40+ year old women covering books, true crime, history, travel and food. It needs to support blog posts, links to social media including YouTube videos, Snapgram, TikTok and Facebook. The background theme needs to be like that of a newspaper. Easy to navigate and to allow me to post blogs/videos.

```html
<!DOCTYPE html>
<html lang="en">
<head>
<meta charset="utf-8">
<title>The Tavery Parlour</title>
<link rel="stylesheet" href="https://fonts.googleapis.com/css2?family=Libre+Caslon+Text:wght@400;700&family=Roboto:wght@400;500;700&display=swap">
<style>
:root{
  --ink:#1b1b1f;
  --text:#333;
  --muted:#666;
  --line:#d6d6d6;
  --paper:#ffffff;
  --hero:#c9c9c9;
  --footer:#1a1a22;
  --photo-a:#8d8a86;
  --photo-b:#5c5955;
  --warm-a:#b08a6a;
  --warm-b:#6d5443;
  --cool-a:#8fa3b8;
  --cool-b:#4f6478;
}
*{box-sizing:border-box;margin:0;padding:0}
html,body{width:1200px;height:4415px;overflow:hidden;background:var(--paper)}
body{position:relative;font-family:"Roboto",Arial,sans-serif;color:var(--text)}
.abs{position:absolute}
.serif{font-family:"Libre Caslon Text",Georgia,serif}
.photo{background:linear-gradient(135deg,var(--photo-a),var(--photo-b))}
.photo.warm{background:linear-gradient(135deg,var(--warm-a),var(--warm-b))}
.photo.cool{background:linear-gradient(135deg,var(--cool-a),var(--cool-b))}
.photo.grey{background:linear-gradient(135deg,#bdbdbd,#6e6e6e)}

/* header */
.logo{left:144px;top:38px;font-family:"Libre Caslon Text",Georgia,serif;font-size:34px;color:var(--ink);letter-spacing:-0.5px}
.nav{left:473px;top:0;display:flex;align-items:center;height:100px}
.nav a{font-size:16px;color:var(--ink);text-decoration:none;margin-right:36px}
.nav a.active{background:#000;color:#fff;height:100px;width:82px;display:flex;align-items:center;justify-content:center;margin-right:36px}
.nav-tools{left:940px;top:44px;display:flex;gap:22px;align-items:center}

/* hero */
.hero{left:144px;top:115px;width:912px;height:540px;background:var(--hero)}
.hero-photo{left:0;top:0;width:470px;height:540px;background:linear-gradient(135deg,#9a9896,#6f6c69)}
.hero-title{left:477px;top:100px;font-size:64px;line-height:78px;color:var(--ink)}
.hero-sub{left:477px;top:278px;font-size:20px;line-height:34px;color:#2a2a2a;width:360px}
.hero-btn{left:477px;top:372px;width:168px;height:54px;border:2px solid var(--ink);border-radius:8px;font-size:14px;font-weight:700;color:var(--ink);display:flex;align-items:center;justify-content:center}
.arrow-btn{width:68px;height:68px;border-radius:50%;background:#fff;display:flex;align-items:center;justify-content:center;box-shadow:0 2px 8px rgba(0,0,0,.15)}

/* categories */
.cats{left:144px;top:663px;width:912px;height:189px;display:flex;gap:7px}
.cat{flex:1;position:relative;color:#fff;font-size:15px;font-weight:700;display:flex;align-items:flex-end;justify-content:center;padding-bottom:36px}
.cat.on{padding-bottom:28px}

/* headings */
.h2{font-family:"Libre Caslon Text",Georgia,serif;font-size:36px;color:var(--ink)}
.h2::after{content:"";display:block;width:66px;height:2px;background:var(--ink);margin-top:16px}

/* cards */
.card{border:1px solid var(--line);background:#fff}
.card-body{padding:14px 14px 14px 27px}
.card-title{font-size:15.5px;line-height:24px;color:var(--ink)}
.date{font-size:11px;color:var(--muted)}
.more{font-size:11px;font-weight:700;color:var(--ink);text-decoration:underline}
.blog-item{display:flex;gap:14px;margin-bottom:14px}
.blog-thumb{width:86px;height:86px;flex:none}

/* videos */
.play{width:60px;height:60px;border-radius:50%;background:var(--ink);display:flex;align-items:center;justify-content:center}
.video-text{font-size:21px;line-height:30px;color:var(--ink);width:860px}
.rule{left:144px;width:912px;height:2px;background:var(--line)}

/* events */
.event{border:1px solid var(--line);padding:22px 18px}
.event h3{font-size:21px;font-weight:500;color:var(--ink);line-height:28px}
.event p{font-size:12.5px;line-height:22.5px;color:var(--muted);text-align:justify;margin-top:14px}

/* clips */
.clip{width:221px;height:302px}
.clip .mini{position:absolute;right:18px;bottom:18px;width:34px;height:34px;border-radius:50%;background:#fff;display:flex;align-items:center;justify-content:center;border:2px solid var(--ink)}
.badge{display:inline-block;width:40px;height:40px;border-radius:8px;background:var(--ink);vertical-align:middle}

/* snap grid */
.grid{left:142px;top:3557px;width:533px;display:grid;grid-template-columns:repeat(3,1fr);gap:7px}
.grid div{height:137px}

/* newsletter */
.field{left:742px;width:312px;height:46px;border:1px solid #999;font-size:13px;color:#333;padding:0 16px;display:flex;align-items:center}
.subscribe{left:742px;top:3672px;width:312px;height:46px;background:var(--ink);color:#fff;font-size:15px;font-weight:700;display:flex;align-items:center;justify-content:center}
.social-box{left:742px;top:3749px;width:312px;height:238px;border:1px solid var(--line)}
.dots{display:flex;gap:12px;justify-content:center;margin-top:40px}
.dots span{width:44px;height:44px;border-radius:50%;display:block}

/* footer */
.footer{left:0;top:4077px;width:1200px;height:338px;background:var(--footer);color:#fff;text-align:center}
.footer-logo{font-family:"Libre Caslon Text",Georgia,serif;font-size:54px;position:absolute;top:70px;width:100%}
.footer-nav{position:absolute;top:186px;width:100%;font-size:18px;display:flex;justify-content:center;gap:26px}
.footer-copy{position:absolute;top:254px;width:100%;font-size:13px}
</style>
</head>
<body>

<header>
  <div class="abs logo">The Tavery Parlour</div>
  <nav class="abs nav">
    <a class="active" href="#">Home</a>
    <a href="#">About</a>
    <a href="#">Blogs</a>
    <a href="#">Articles</a>
    <a href="#">Contact Us</a>
  </nav>
  <div class="abs nav-tools">
    <svg width="38" height="14" viewBox="0 0 38 14"><rect width="22" height="14" fill="#2b3a8c"/><rect x="9" width="4" height="14" fill="#fff"/><rect y="5" width="22" height="4" fill="#fff"/><rect x="10" width="2" height="14" fill="#c8102e"/><rect y="6" width="22" height="2" fill="#c8102e"/><path d="M28 5l4 4 4-4z" fill="#1b1b1f"/></svg>
    <svg width="16" height="16" viewBox="0 0 16 16" fill="none" stroke="#1b1b1f" stroke-width="1.4"><circle cx="8" cy="5" r="3.5"/><path d="M1.5 15c1-4 12-4 13 0"/></svg>
    <svg width="16" height="16" viewBox="0 0 16 16" fill="none" stroke="#1b1b1f" stroke-width="1.6"><circle cx="7" cy="7" r="5"/><path d="M11 11l4 4"/></svg>
  </div>
</header>

<section class="abs hero">
  <div class="abs hero-photo" role="img" aria-label="Photo of an older woman exercising on a yoga mat"></div>
  <h1 class="abs hero-title serif" style="font-weight:400">The Tavery<br>Parlour</h1>
  <p class="abs hero-sub">Sed ut perspiciatis unde omnis iste natus error sit voluptatem</p>
  <div class="abs hero-btn">GET STARTED</div>
</section>
<div class="abs arrow-btn" style="left:103px;top:352px"><svg width="24" height="16" viewBox="0 0 24 16" fill="none" stroke="#1b1b1f" stroke-width="2"><path d="M23 8H2M8 2L2 8l6 6"/></svg></div>
<div class="abs arrow-btn" style="left:1027px;top:352px"><svg width="24" height="16" viewBox="0 0 24 16" fill="none" stroke="#1b1b1f" stroke-width="2"><path d="M1 8h21M16 2l6 6-6 6"/></svg></div>

<div class="abs cats">
  <div class="cat photo grey" role="img" aria-label="Woman reading a book">BOOKS</div>
  <div class="cat photo grey" role="img" aria-label="Woman in thought">TRUE CRIME</div>
  <div class="cat on photo" style="background:linear-gradient(135deg,#c4b9ad,#8a7c70)" role="img" aria-label="Two women looking at an old album">HISTORY&nbsp;&nbsp;<svg width="24" height="24" viewBox="0 0 24 24" fill="none" stroke="#fff" stroke-width="1.6" style="margin-left:10px"><circle cx="12" cy="12" r="10"/><path d="M10 7l5 5-5 5"/></svg></div>
  <div class="cat photo grey" role="img" aria-label="Smiling woman on a trip">TRAVEL</div>
  <div class="cat photo grey" role="img" aria-label="Friends sharing a meal">FOOD</div>
</div>

<h2 class="abs h2" style="left:142px;top:922px;font-weight:400">Top Stories</h2>
<h2 class="abs h2" style="left:782px;top:922px;font-weight:400">Latest Blogs</h2>

<article class="abs card" style="left:144px;top:1006px;width:305px;height:324px">
  <div class="photo warm" style="height:212px" role="img" aria-label="Older woman at home beside flowers"></div>
  <div class="card-body">
    <div class="card-title">Lorem ipsum dolor sit amedipiscing commodo consequ</div>
    <div class="date" style="margin-top:6px">December 02,2024</div>
    <div class="more" style="text-align:right;margin-top:2px;padding-right:6px">READ MORE</div>
  </div>
</article>
<article class="abs card" style="left:464px;top:1006px;width:306px;height:324px">
  <div class="photo cool" style="height:212px" role="img" aria-label="Smiling woman at a breakfast table"></div>
  <div class="card-body">
    <div class="card-title">Lorem ipsum dolor sit amedipiscing commodo consequ</div>
    <div class="date" style="margin-top:6px">December 02,2024</div>
    <div class="more" style="text-align:right;margin-top:2px;padding-right:6px">READ MORE</div>
  </div>
</article>
<aside class="abs card" style="left:782px;top:1006px;width:274px;height:324px;padding:16px 14px">
  <div class="blog-item"><div class="blog-thumb photo" style="background:linear-gradient(135deg,#444,#1f1f24)" role="img" aria-label="Woman in low light"></div><div><div class="card-title">Sed ut perspiciatis unde ote natus</div><div class="date">December 02,2024</div></div></div>
  <div class="blog-item"><div class="blog-thumb photo warm" role="img" aria-label="Portrait of an older woman"></div><div><div class="card-title">Lorem ipsum dolor sit amedipiscing</div><div class="date">December 02,2024</div></div></div>
  <div class="blog-item"><div class="blog-thumb photo cool" role="img" aria-label="Woman outdoors"></div><div><div class="card-title">Nemo enim ipsamv oluptatem quia</div><div class="date">December 02,2024</div></div></div>
</aside>

<div class="abs photo" style="left:144px;top:1342px;width:912px;height:398px;background:linear-gradient(90deg,#d9d9d9,#8f8f8f 55%,#3d4d6a)" role="img" aria-label="Video still of a woman holding a camera"></div>
<div class="abs serif" style="left:200px;top:1514px;font-size:40px;color:#1b1b1f">The Tavery Parlour</div>
<div class="abs play" style="left:648px;top:1511px"><svg width="20" height="22" viewBox="0 0 20 22"><path d="M2 1l17 10L2 21z" fill="#fff"/></svg></div>
<p class="abs video-text" style="left:172px;top:1755px">Lorem ipsum dolor sit amedipiscingcommodo conseququia consequuntur magni dolores eos qui ratione voluptatem sequi nesciunt</p>
<div class="abs date" style="left:172px;top:1838px">December 02,2024</div>
<div class="abs more" style="left:962px;top:1838px">READ MORE</div>
<div class="abs rule" style="top:1892px"></div>

<h2 class="abs h2" style="left:144px;top:1962px;font-weight:400">Latest Events</h2>
<h2 class="abs h2" style="left:432px;top:1962px;font-weight:400">Highlights</h2>
<h2 class="abs h2" style="left:782px;top:1962px;font-weight:400">Popular Events</h2>

<article class="abs event" style="left:144px;top:2045px;width:274px;height:326px">
  <h3>Nemo enim iptatuia</h3>
  <div class="date">December 02,2024</div>
  <p>Nemo enim ipsam voluptatem quia voluptas sit aspernatur aut odit aut fugit, sed quia nsequuntur magni dolores eos qui ratione voluptatelt, sed quia nsequuntur magni dolores eos qui ratione volupit, sed quia nsequuntur magni dolores eos qui ratione volupit, sed quia nsequuntur a nsequuntur magni dolores eos qui ratione volupit, sed quia nsequuntur magni <span class="more">READ MORE</span></p>
</article>
<article class="abs event" style="left:430px;top:2045px;width:340px;height:326px">
  <div style="width:160px">
    <h3>Nemo esamvolu ptatem quia</h3>
    <div class="date">December 02,2024</div>
    <p>Nemo enim ipsam voluptatem quia voluptas sit aspernatur aut odit aut fugit, sed quia nsequuntur magni dolores eos qui ratione voluptateit, sed quia nsequuntur magni dolores eos qui ratione volupit, sed quia nsequuntur</p>
  </div>
  <div class="abs photo grey" style="left:214px;top:14px;width:110px;height:296px" role="img" aria-label="Woman reading a book"></div>
</article>
<article class="abs event" style="left:782px;top:2045px;width:274px;height:326px">
  <h3>Nemo enim iptatuia</h3>
  <div class="date">December 02,2024</div>
  <p>Nemo enim ipsam voluptatem quia voluptas sit aspernatur aut odit aut fugit, sed quia nsequuntur magni dolores eos qui ratione voluptatelt, sed quia nsequuntur magni dolores eos qui ratione volupit, sed quia nsequuntur magni dolores eos qui ratione volupit, sed quia nsequuntur a nsequuntur magni dolores eos qui ratione volupit, sed quia nsequuntur magni <span class="more">READ MORE</span></p>
</article>

<div class="abs photo" style="left:144px;top:2390px;width:912px;height:396px;background:linear-gradient(135deg,#7d7d82,#3c3c40)" role="img" aria-label="Video still of a woman in sunglasses for a true crime story"></div>
<div class="abs play" style="left:570px;top:2558px"><svg width="20" height="22" viewBox="0 0 20 22"><path d="M2 1l17 10L2 21z" fill="#fff"/></svg></div>
<p class="abs video-text" style="left:172px;top:2809px">Lorem ipsum dolor sit amedipiscingcommodo conseququia consequuntur magni dolores eos qui ratione voluptatem sequi nesciunt</p>
<div class="abs date" style="left:172px;top:2891px">December 02,2024</div>
<div class="abs more" style="left:970px;top:2891px">READ MORE</div>
<div class="abs rule" style="top:2935px"></div>

<div class="abs" style="left:142px;top:2996px;display:flex;align-items:center;gap:18px">
  <span class="badge"></span><span class="serif" style="font-size:36px;color:#1b1b1f">ClipReel</span>
</div>
<svg class="abs" style="left:1002px;top:3008px" width="58" height="16" viewBox="0 0 58 16" fill="none" stroke="#555" stroke-width="1.5"><path d="M22 8H2M7 3L2 8l5 5M36 8h20M51 3l5 5-5 5"/></svg>

<div class="abs clip photo warm" style="left:142px;top:3084px" role="img" aria-label="Woman reading and smiling"><span class="mini"><svg width="10" height="12" viewBox="0 0 10 12"><path d="M1 1l8 5-8 5z" fill="#1b1b1f"/></svg></span></div>
<div class="abs clip photo" style="left:374px;top:3084px;background:linear-gradient(180deg,#b8b8b8,#2a2a2e)" role="img" aria-label="Woman in a winter scarf">
  <span class="abs" style="left:93px;top:165px;width:34px;height:34px;border-radius:50%;background:#fff;display:flex;align-items:center;justify-content:center"><svg width="10" height="12" viewBox="0 0 10 12"><path d="M1 1l8 5-8 5z" fill="#1b1b1f"/></svg></span>
  <span class="abs" style="left:0;top:210px;width:221px;text-align:center;color:#fff;font-size:14px;font-weight:500;line-height:24px">Lorem ipsum dolor<br>sit volputum</span>
</div>
<div class="abs clip photo" style="left:605px;top:3084px;background:linear-gradient(135deg,#8a8466,#4d4a3b)" role="img" aria-label="Woman reading on a sofa"><span class="mini"><svg width="10" height="12" viewBox="0 0 10 12"><path d="M1 1l8 5-8 5z" fill="#1b1b1f"/></svg></span></div>
<div class="abs clip photo" style="left:837px;top:3084px;background:linear-gradient(135deg,#d2c8b4,#8a7a62)" role="img" aria-label="Woman enjoying a meal"><span class="mini"><svg width="10" height="12" viewBox="0 0 10 12"><path d="M1 1l8 5-8 5z" fill="#1b1b1f"/></svg></span></div>

<div class="abs" style="left:142px;top:3487px;display:flex;align-items:center;gap:18px">
  <span class="badge"></span><span class="serif" style="font-size:36px;color:#1b1b1f">Follow Us on Snapgram</span>
</div>
<div class="abs grid">
  <div class="photo warm" role="img" aria-label="Woman with binoculars outdoors"></div>
  <div class="photo" style="background:linear-gradient(135deg,#3a3a40,#1c1c22)" role="img" aria-label="Friends at a night gathering"></div>
  <div class="photo cool" role="img" aria-label="Woman relaxing by the sea"></div>
  <div class="photo warm" role="img" aria-label="Woman smiling in a field"></div>
  <div class="photo" style="background:linear-gradient(135deg,#d8c9b0,#9b8468)" role="img" aria-label="Friends laughing in a cafe"></div>
  <div class="photo" style="background:linear-gradient(135deg,#a5988a,#4f463e)" role="img" aria-label="Women shopping together"></div>
  <div class="photo cool" role="img" aria-label="Woman reading by a window"></div>
  <div class="photo" style="background:linear-gradient(135deg,#c9a45e,#5f4c2a)" role="img" aria-label="Two friends on a hillside at sunset"></div>
  <div class="photo warm" role="img" aria-label="Woman eating at a market"></div>
</div>

<h2 class="abs serif" style="left:742px;top:3472px;font-size:36px;font-weight:400;color:#1b1b1f">Newsletter Sign Up</h2>
<div class="abs field" style="top:3557px">Enter Name</div>
<div class="abs field" style="top:3614px">Enter Email</div>
<div class="abs subscribe">SUBSCRIBE</div>
<div class="abs social-box">
  <div class="serif" style="text-align:center;font-size:36px;color:#1b1b1f;margin-top:44px">Social Media</div>
  <div class="dots" role="img" aria-label="Social media links">
    <span style="background:#3b5998"></span>
    <span style="background:#c13584"></span>
    <span style="background:#d62a2a"></span>
    <span style="background:#111"></span>
  </div>
</div>

<footer class="abs footer">
  <div class="footer-logo">The Tavery Parlour</div>
  <nav class="footer-nav"><span>HOME</span><span>/</span><span>ABOUT</span><span>/</span><span>BLOGS</span><span>/</span><span>ARTICLES</span><span>/</span><span>CONTACT US</span></nav>
  <div class="footer-copy">© 2025 Companyname.All rights reserved.Privacy &nbsp;|&nbsp; Terms of Use</div>
</footer>

</body>
</html>
```